First Annual Pemberton Family Reunion

Family reunion invitation, please see the attached letter for the language. Also provided a picture of my grandparents, if you could include it on a letter or brochure. I'm flexible.
Updates

I just uploaded a Word document with the time, address, and list of activities. Please click on the hyperlink, it takes you directly to our Family Reunion webpage and click on Agenda for all details.

Target Market(s)

Family and Friends invitation

Requirements
Must have
• Date, time, picture, family logo, and website for payment

```html
<!DOCTYPE html>
<html lang="en">
<head>
<meta charset="utf-8">
<title>Pemberton Family Reunion — Invitation Brochure</title>
<link href="https://fonts.googleapis.com/css2?family=Cinzel:wght@400;700&family=Great+Vibes&family=Montserrat:wght@400;600;800&family=Tinos&display=swap" rel="stylesheet">
<style>
  :root {
    --purple: #5210a8;
    --cream: #fbf8f5;
    --paper: #ffffff;
    --ink: #111111;
    --stage: #e6e4e3;
    --photo-warm: #a5735a;
    --photo-cool: #3d5f8f;
    --photo-dark: #4a3a36;
  }
  * { box-sizing: border-box; margin: 0; padding: 0; }
  html, body { width: 1200px; height: 1200px; overflow: hidden; }
  body { background: var(--stage); position: relative; font-family: "Montserrat", sans-serif; color: var(--ink); }

  .spread { position: absolute; width: 634px; height: 490px; display: flex; }
  .spread--cover { left: 182px; top: 90px; }
  .spread--inside { left: 385px; top: 619px; }
  .page { position: relative; width: 317px; height: 490px; overflow: hidden; }
  .page--cream { background: var(--cream); }
  .page--white { background: var(--paper); }

  .wordmark { position: absolute; left: 0; right: 0; font-family: "Cinzel", serif; font-weight: 700; color: var(--ink); display: flex; align-items: center; justify-content: center; gap: 8px; text-align: center; }
  .wordmark__square { width: 11px; height: 11px; background: var(--ink); flex: none; }
  .wordmark--cover { top: 82px; font-size: 16px; letter-spacing: 1px; line-height: 20px; }
  .wordmark--letter { top: 56px; font-size: 11px; letter-spacing: 1px; }

  .tagline { position: absolute; top: 222px; left: 0; right: 0; text-align: center; font-family: "Cinzel", serif; font-weight: 400; color: var(--purple); font-size: 15.5px; line-height: 20px; }
  .intro { position: absolute; top: 276px; left: 30px; right: 30px; text-align: center; font-size: 8.5px; line-height: 12.2px; }
  .intro strong { color: var(--purple); font-weight: 800; }

  .registration { position: absolute; top: 405px; left: 0; right: 0; text-align: center; }
  .registration__small { color: var(--purple); font-weight: 800; font-size: 8px; line-height: 10px; }
  .registration__big { font-weight: 800; font-size: 14px; line-height: 17px; }
  .registration__email { display: inline-block; margin-top: 4px; background: var(--purple); color: #fff; font-size: 9px; line-height: 12px; padding: 2px 13px; border-radius: 9px; }
  .registration__email b { font-weight: 800; }

  .cover-band { position: absolute; left: 0; width: 317px; }
  .cover-band--top { top: 0; height: 128px; }
  .cover-band--bottom { bottom: 0; height: 100px; }

  .cover-title { position: absolute; top: 26px; left: 0; width: 317px; text-align: center; color: #fff; }
  .cover-title__script { font-family: "Great Vibes", cursive; font-size: 29px; line-height: 36px; }
  .cover-title__caps { font-family: "Cinzel", serif; font-size: 12px; letter-spacing: 6px; margin-top: 4px; }
  .cover-badge { position: absolute; top: 14px; right: 12px; width: 44px; height: 44px; background: #fff; color: var(--ink); font-family: "Cinzel", serif; font-weight: 700; font-size: 6px; line-height: 8px; display: flex; align-items: center; justify-content: center; text-align: center; }

  .photo-grid { position: absolute; left: 60px; top: 166px; width: 195px; height: 194px; display: grid; grid-template-columns: repeat(3, 1fr); gap: 5px; }
  .photo-col { display: flex; flex-direction: column; gap: 5px; }
  .photo--warm { background: linear-gradient(160deg, #b5484a, var(--photo-warm)); }
  .photo--cool { background: linear-gradient(160deg, #2f4f86, var(--photo-cool)); }
  .photo--dark { background: linear-gradient(160deg, #625250, var(--photo-dark)); }
  .photo--green { background: linear-gradient(160deg, #7c8f5a, #6a5a48); }

  .event-details { position: absolute; top: 404px; left: 0; right: 0; text-align: center; color: #fff; font-family: "Cinzel", serif; font-size: 7.5px; line-height: 9.5px; }
  .event-details__label { font-weight: 700; }
  .event-details__time { display: flex; align-items: center; justify-content: center; gap: 5px; margin: 2px 0; }
  .event-details__time::before, .event-details__time::after { content: ""; width: 28px; height: 1px; background: #fff; }
  .event-details__rsvp { font-family: "Montserrat", sans-serif; font-weight: 800; font-size: 6px; }

  .family-tree { position: absolute; left: 34px; top: 121px; width: 269px; height: 248px; border-radius: 46% 46% 12% 12%; background: radial-gradient(circle at 50% 40%, #c9b4ea, #e9e0f6 75%); }

  .letter { position: absolute; left: 26px; top: 118px; width: 270px; font-family: "Tinos", serif; font-size: 6.8px; line-height: 8.6px; color: #222; }
  .letter__date { text-align: center; font-size: 13px; line-height: 16px; margin-bottom: 3px; padding-left: 40px; color: var(--ink); }
  .letter p { margin-bottom: 8px; }
  .letter a { color: var(--purple); text-decoration: none; }
</style>
</head>
<body>

<section class="spread spread--cover">
  <div class="page page--cream">
    <div class="wordmark wordmark--cover"><span class="wordmark__square"></span><span>Pemberton Family<br>Reunion</span></div>
    <h2 class="tagline">Friends come and go,<br>but family lasts forever!</h2>
    <p class="intro">Come join the extended Pemberton family for our<br><strong>1ST ANNUAL FAMILY REUNION!</strong><br>Be prepared for hugs, laughter and catching-up<br>that's long overdue!</p>
    <div class="registration">
      <div class="registration__small">REGISTRATION IS</div>
      <div class="registration__big">NOW OPEN!</div>
      <div class="registration__email">info@<b>pembertonreunion</b>.net</div>
    </div>
  </div>

  <div class="page page--white">
    <svg class="cover-band cover-band--top" viewBox="0 0 317 128" preserveAspectRatio="none">
      <path d="M0 0H317V118L300 112 283 120 265 110 245 116 227 106 207 114 186 108 164 118 144 109 122 115 102 107 80 117 58 110 36 119 18 111 0 116Z" fill="#e9e9ec"/>
      <path d="M0 0H317V111L300 106 283 113 265 103 245 109 227 99 207 107 186 101 164 111 144 102 122 108 102 100 80 110 58 103 36 112 18 104 0 109Z" fill="var(--purple)"/>
    </svg>
    <div class="cover-title">
      <div class="cover-title__script">Pemberton Family</div>
      <div class="cover-title__caps">REUNION</div>
    </div>
    <div class="cover-badge">Pemberton<br>Family<br>Reunion</div>

    <div class="photo-grid">
      <div class="photo-col">
        <div class="photo photo--warm" role="img" aria-label="Family group photo" style="flex:1.6"></div>
        <div class="photo photo--dark" role="img" aria-label="Couple photo" style="flex:1.1"></div>
        <div class="photo photo--cool" role="img" aria-label="Family gathering photo" style="flex:0.5"></div>
      </div>
      <div class="photo-col">
        <div class="photo photo--dark" role="img" aria-label="Portrait of a family member" style="flex:1.1"></div>
        <div class="photo photo--warm" role="img" aria-label="Grandparents photo" style="flex:1"></div>
        <div class="photo photo--green" role="img" aria-label="Family members outdoors" style="flex:1"></div>
      </div>
      <div class="photo-col">
        <div class="photo photo--cool" role="img" aria-label="Graduation photo" style="flex:1"></div>
        <div class="photo photo--warm" role="img" aria-label="Family selfie" style="flex:1"></div>
      </div>
    </div>

    <svg class="cover-band cover-band--bottom" viewBox="0 0 317 100" preserveAspectRatio="none">
      <path d="M0 6L20 0 40 8 60 2 82 10 104 3 126 9 146 1 168 8 190 2 212 9 234 1 256 8 278 2 298 9 317 4V100H0Z" fill="#e9e9ec"/>
      <path d="M0 12L20 5 40 13 60 7 82 15 104 8 126 14 146 6 168 13 190 7 212 14 234 6 256 13 278 7 298 14 317 9V100H0Z" fill="var(--purple)"/>
    </svg>
    <div class="event-details">
      <div class="event-details__label">Date:</div>
      <div>From September 1, 2023,<br>through September 3, 2023</div>
      <div class="event-details__time">Time: 3:00 PM</div>
      <div class="event-details__rsvp">RSVP</div>
      <div class="event-details__label">Pay your Deposit:</div>
      <div>www.pembertonreunion.net</div>
    </div>
  </div>
</section>

<section class="spread spread--inside">
  <div class="page page--cream">
    <div class="family-tree" role="img" aria-label="Purple family tree illustration with framed family photos on its branches"></div>
  </div>

  <div class="page page--cream">
    <div class="wordmark wordmark--letter"><span class="wordmark__square"></span><span>Pemberton Family Reunion</span></div>
    <div class="letter">
      <div class="letter__date">April 7, 2023</div>
      <p>Dear Family,</p>
      <p>I hope this letter finds all of you in good health and high spirits. Our family, which is spread across different parts of the country, rarely gets an opportunity to gather together under one roof, but I am excited to inform you that we have finally planned a family reunion.</p>
      <p>It has been long overdue, and we are looking forward to catching up with everyone, reminiscing old memories, and creating some new ones over the course of this event. I cannot emphasize enough on how important this reunion will be for our family. We have come to learn over the years that nothing can ever replace the love and connections that we share between us.</p>
      <p>Our family reunion will be from September 1, 2023, through September 3, 2023. We will have a fun-filled weekend filled with activities for all ages, which will include games, music, storytelling, and much more. It is a chance for our family to get to know new members, spend time with those we know and love, and to make it a memorable experience.</p>
      <p>Please RSVP and pay your deposit as soon as possible at <a href="#">https://pembertonreunion.net</a> so that we can make arrangements accordingly. Also, please notify any family members who may have been left out or forgotten.</p>
      <p>I cannot wait to see all of you soon and spend quality time together as a family.</p>
      <p>As ever,</p>
      <p>The Pemberton Family Committee</p>
    </div>
  </div>
</section>

</body>
</html>
```